Tranquil Pathways Hypnotherapy Business Card

Logo attached. (will be printing onto thick white/off white textured card)

Double sided business card for two Therapists working at Tranquil Pathways Hypnotherapy.

Require one design, but with different name and mobile numbers on each card.

Target Market(s)

Medical, Health

Industry/Entity Type

Business

Contact Information for Business Card

Need one business card design, but a separate card for each person - Darren Whitfield and Marike de Bruyn.

FRONT OF CARD

Logo

Name (Darren Whitfield on one card, Marike de Bruyn on the other)
Professional Clinical Hypnotherapist

Consulting Rooms (Near Larkmoor Hospital)
284 Bellcrest Avenue
Elmsbrook VIC 3187

Darren@TranquilPathwaysHypno.com.au OR Marike@TranquilPathwaysHypno.com.au

Mobile: 0427 862 491 (for Darren) OR
Mobile: 0438 574 206 (for Marike)

BACK OF CARD

Logo

Website: www.TranquilPathwaysHypno.com.au

Phone: 1300 748 519

Requirements
Must have
• Text and logo only. No additiional graphics.

```html
<!DOCTYPE html>
<html lang="en">
<head>
<meta charset="utf-8">
<title>Tranquil Pathways Hypnotherapy – Business Card</title>
<link rel="stylesheet" href="https://fonts.googleapis.com/css2?family=Source+Sans+3:wght@400;600;700&display=swap">
<style>
  :root {
    --navy: #1f2a63;
    --white: #ffffff;
    --grey: #5d5f66;
    --ink: #2a2c33;
    --rule: #7a7c84;
    --backdrop: #e9e7e3;
  }
  * { box-sizing: border-box; margin: 0; padding: 0; }
  html, body { width: 1200px; height: 900px; overflow: hidden; }
  body {
    background: var(--backdrop);
    font-family: "Source Sans 3", Arial, sans-serif;
    display: flex;
    align-items: center;
    justify-content: center;
    gap: 40px;
  }
  .card {
    width: 540px;
    height: 330px;
    position: relative;
    overflow: hidden;
    box-shadow: 0 6px 18px rgba(0,0,0,.18);
  }

  /* Shared brand lettering */
  .brand { display: flex; align-items: center; gap: 14px; }
  .brand-rule { width: 2px; align-self: stretch; }
  .brand-name {
    font-weight: 700;
    text-transform: uppercase;
    line-height: 1.05;
    font-size: 22px;
    letter-spacing: .5px;
  }

  /* Back side */
  .card--back { background: var(--navy); }
  .card--back .brand {
    position: absolute; top: 40px; left: 0; right: 0; height: 80px;
    justify-content: center;
  }
  .card--back .brand-dot { width: 76px; height: 76px; border-radius: 50%; background: var(--white); }
  .card--back .brand-rule { background: var(--white); }
  .card--back .brand-name { color: var(--white); }
  .band {
    position: absolute; left: 0; right: 0;
    display: flex; align-items: center; justify-content: center; gap: 8px;
  }
  .band--web { top: 160px; height: 56px; background: var(--white); color: var(--navy); font-size: 16px; }
  .band--phone { top: 216px; height: 46px; color: var(--white); font-size: 16px; font-weight: 600; }
  .band--plain { top: 262px; height: 36px; background: var(--white); }

  /* Front side */
  .card--front { background: var(--white); }
  .card--front .brand {
    position: absolute; top: 30px; left: 34px; height: 100px;
  }
  .card--front .brand-dot {
    width: 100px; height: 100px; border-radius: 50%; background: var(--navy);
  }
  .card--front .brand-rule { background: var(--rule); }
  .card--front .brand-name { color: var(--navy); font-size: 24px; }
  .details {
    position: absolute; left: 276px; top: 146px;
    color: var(--ink); font-size: 13.5px; line-height: 1.25;
  }
  .person-name {
    color: var(--navy); font-weight: 700; font-size: 18px; text-transform: uppercase;
  }
  .person-role { color: var(--grey); font-size: 13.5px; margin-bottom: 16px; }
  .address { margin-bottom: 12px; }
  .contact-row { display: flex; align-items: center; gap: 7px; }
  .contact-row svg { flex: none; }
</style>
</head>
<body>

  <section class="card card--back" aria-label="Card back">
    <div class="brand">
      <span class="brand-dot"></span>
      <span class="brand-rule"></span>
      <span class="brand-name">Tranquil Pathways<br>Hypnotherapy</span>
    </div>
    <p class="band band--web">www.TranquilPathwaysHypno.com.au</p>
    <p class="band band--phone">
      <svg width="14" height="14" viewBox="0 0 24 24" aria-hidden="true"><path fill="#ffffff" d="M6.6 10.8a15.2 15.2 0 0 0 6.6 6.6l2.2-2.2a1 1 0 0 1 1-.25 11.4 11.4 0 0 0 3.6.57 1 1 0 0 1 1 1V20a1 1 0 0 1-1 1A17 17 0 0 1 3 4a1 1 0 0 1 1-1h3.5a1 1 0 0 1 1 1c0 1.25.2 2.45.57 3.57a1 1 0 0 1-.25 1z"/></svg>
      1300 748 519
    </p>
    <div class="band band--plain"></div>
  </section>

  <section class="card card--front" aria-label="Card front">
    <div class="brand">
      <span class="brand-dot"></span>
      <span class="brand-rule"></span>
      <span class="brand-name">Tranquil Pathways<br>Hypnotherapy</span>
    </div>
    <div class="details">
      <p class="person-name">Darren Whitfield</p>
      <p class="person-role">Professional Clinical Hypnotherapist</p>
      <p class="address">Consulting Rooms<br>284 Bellcrest Avenue<br>Elmsbrook VIC 3187</p>
      <p class="contact-row">
        <svg width="13" height="13" viewBox="0 0 24 24" aria-hidden="true"><path fill="#1f2a63" d="M6.6 10.8a15.2 15.2 0 0 0 6.6 6.6l2.2-2.2a1 1 0 0 1 1-.25 11.4 11.4 0 0 0 3.6.57 1 1 0 0 1 1 1V20a1 1 0 0 1-1 1A17 17 0 0 1 3 4a1 1 0 0 1 1-1h3.5a1 1 0 0 1 1 1c0 1.25.2 2.45.57 3.57a1 1 0 0 1-.25 1z"/></svg>
        0427 862 491
      </p>
      <p class="contact-row">
        <svg width="13" height="13" viewBox="0 0 24 24" aria-hidden="true"><rect x="2" y="5" width="20" height="14" fill="#1f2a63"/><path d="M2 5l10 8 10-8" fill="none" stroke="#fff" stroke-width="1.6"/></svg>
        Darren@TranquilPathwaysHypno.com.au
      </p>
    </div>
  </section>

</body>
</html>
```